Instant Broth for Ramen and Soup - Need labels for three flavors

We are a new company planning to launch a line of all natural powdered instant broth for ramen and soups. We need a logo design for our three launch flavors which will be Chicken, Prime Beef and Garden Vegetable. The powdered broth will be sold in 4oz containers with a white cap.
We would like the logo to be at the top of the label and or product description "Instant Broth for Ramen and Soups" underneath. The product description should stand out to the consumer, so it should likely be a larger font and one that compliments the logo. Below the Product description, we would like the name of the flavor and appropriate color scheme to match the flavor (see product picture for color). The design for each flavor should be the same, the only thing that should change is the color scheme to match flavor. Because we use all natural ingredients we would also like the label to state "Natural Ingredients" and "Gluten Free" on the front.
Additionally if you could please include placeholders for the nutritional label, ingredients list beneath, net size/weight on the side, bar code and a placeholder address for "Wexley Pantry LLC" that would be great as we are still finalizing these details. We would also like the label design to be catchy and interesting while complimenting the fun light-hearted logo.
Lastly, if your design is chosen you will be our main choice for additional design work (if you wish) including, top label design for the cap, finalizing the product info, formatting actual jar dimensions and other design work for the many other additional flavors we will be releasing.
Target Market(s)
Homemade ramen and soup connoisseurs, health conscious consumers, millennials and college students
Industry/Entity Type
It Company
Other font styles liked:
- SingleSleeve
Colors
Designer to choose colors to be used in the design.
Requirements
Must have
- 1) Logo
- 2) Product description "Instant Broth for Ramen and Soups"
- 3) Flavor title and color scheme
- 4) "Natural Ingredients" and "Gluten Free"
- 5) Place holder info for BQH required information (nutrition facts, net weight etc.)
Nice to have
- 1) Instructions (placeholder)
- 2) Additional info about the product (placeholder)

```html
<!DOCTYPE html>
<html lang="en">
<head>
<meta charset="utf-8">
<title>Instant Broth Labels</title>
<link href="https://fonts.googleapis.com/css2?family=Oswald:wght@400;500&family=Kaushan+Script&family=Roboto:wght@700&display=swap" rel="stylesheet">
<style>
  :root {
    --page: #ffffff;
    --white: #ffffff;
    --brand-ink: #3b3aa0;
    --net-ink: #3a2a10;
    --veg-dark: #136a0c;
    --veg-mid: #2a9619;
    --veg-bright: #74c52a;
    --veg-light: #c9df72;
    --veg-title-edge: #1f6e12;
    --veg-accent: #f2e21e;
    --veg-tag: #f3c20f;
    --veg-tag-ink: #1d5a0f;
    --veg-bowl: #d8b25a;
    --chk-dark: #e35206;
    --chk-mid: #ec7112;
    --chk-bright: #f0921c;
    --chk-light: #f2c145;
    --chk-title-edge: #c2470a;
    --chk-accent: #2a2f9a;
    --chk-tag: #2c3fa4;
    --chk-tag-ink: #ffffff;
    --chk-tag-sub: #f3e01a;
    --chk-bowl: #e8cf7a;
  }
  * { margin: 0; padding: 0; box-sizing: border-box; }
  html, body { width: 1200px; height: 1000px; overflow: hidden; background: var(--page); }
  .canvas { position: relative; width: 1200px; height: 1000px; }

  .label {
    position: absolute; left: 72px; width: 1065px; height: 352px; overflow: hidden;
    background: linear-gradient(90deg, var(--dark) 0%, var(--dark) 30%, var(--mid) 62%, var(--bright) 100%);
  }
  .label--vegetable { top: 141px;
    --dark: var(--veg-dark); --mid: var(--veg-mid); --bright: var(--veg-bright); --light: var(--veg-light);
    --edge: var(--veg-title-edge); --accent: var(--veg-accent); --tag: var(--veg-tag);
    --tag-ink: var(--veg-tag-ink); --tag-sub: var(--white); --bowl: var(--veg-bowl); }
  .label--chicken { top: 541px;
    --dark: var(--chk-dark); --mid: var(--chk-mid); --bright: var(--chk-bright); --light: var(--chk-light);
    --edge: var(--chk-title-edge); --accent: var(--chk-accent); --tag: var(--chk-tag);
    --tag-ink: var(--chk-tag-ink); --tag-sub: var(--chk-tag-sub); --bowl: var(--chk-bowl); }

  .label__sweep { position: absolute; inset: 0; }

  .instruction-heading {
    position: absolute; left: 51px; top: 48px;
    font: 700 13px "Roboto", Arial, sans-serif; color: var(--white); letter-spacing: .2px;
  }
  .nutrition-panel {
    position: absolute; left: 273px; top: 25px; width: 217px; height: 308px;
    background: var(--white); border-radius: 8px; padding: 17px 17px;
  }
  .nutrition-panel__title { font: 700 12.5px "Roboto", Arial, sans-serif; color: var(--dark); }

  .brand-name {
    position: absolute; left: 696px; top: 40px;
    font: 700 20px "Roboto", Arial, sans-serif; color: var(--brand-ink);
  }

  .title { position: absolute; left: 540px; top: 92px; width: 300px; height: 130px; transform: rotate(-5deg); transform-origin: left bottom; }
  .title__instant { position: absolute; left: 88px; top: 2px; font: 500 25px "Oswald", sans-serif; color: var(--accent); letter-spacing: .5px; }
  .title__broth {
    position: absolute; left: 20px; top: 10px; font: 400 80px/1 "Kaushan Script", cursive; color: var(--white);
    text-shadow: -2px -2px 0 var(--edge), 2px -2px 0 var(--edge), -2px 2px 0 var(--edge), 3px 3px 0 var(--edge);
  }
  .title__sub { position: absolute; left: 8px; top: 92px; font: 700 19px "Roboto", Arial, sans-serif; color: var(--white); white-space: nowrap; }

  .flavor-tag { position: absolute; left: 540px; top: 222px; width: 130px; height: 44px; }
  .flavor-tag svg { position: absolute; inset: 0; }
  .flavor-tag__name { position: absolute; left: 12px; top: 2px; font: 500 18px/1.2 "Oswald", sans-serif; color: var(--tag-ink); transform: rotate(-4deg); }
  .flavor-tag__sub { position: absolute; left: 34px; top: 24px; font: 400 11px/1 "Oswald", sans-serif; color: var(--tag-sub); transform: rotate(-4deg); }

  .claims { position: absolute; right: 338px; top: 283px; text-align: right; }
  .claim { display: flex; justify-content: flex-end; align-items: center; gap: 7px; font: 400 16px/20px "Oswald", sans-serif; color: var(--white); }
  .claim svg { width: 15px; height: 15px; }

  .product-photo { position: absolute; left: 733px; top: 114px; width: 290px; height: 192px; }

  .net-weight { position: absolute; right: 32px; top: 300px; text-align: right; font: 400 14px/17px "Oswald", sans-serif; color: var(--net-ink); }
</style>
</head>
<body>
<main class="canvas">

  <section class="label label--vegetable">
    <svg class="label__sweep" viewBox="0 0 1065 352" preserveAspectRatio="none" aria-hidden="true">
      <defs>
        <linearGradient id="veg-sweep" x1="0" y1="1" x2="1" y2="0">
          <stop offset="0" stop-color="var(--veg-light)"/>
          <stop offset="1" stop-color="var(--veg-bright)"/>
        </linearGradient>
      </defs>
      <path d="M650 352 C690 250 820 175 1065 140 L1065 352 Z" fill="url(#veg-sweep)"/>
    </svg>
    <h3 class="instruction-heading">INSTRUCTION</h3>
    <div class="nutrition-panel"><h3 class="nutrition-panel__title">NUTRITION FACTS</h3></div>
    <div class="brand-name">Wexley Pantry</div>
    <div class="title">
      <span class="title__instant">INSTANT</span>
      <span class="title__broth">Broth</span>
      <span class="title__sub">for Ramen and Soups</span>
    </div>
    <div class="flavor-tag">
      <svg viewBox="0 0 130 44" aria-hidden="true"><path d="M0 12 L128 0 L120 36 L4 44 Z" fill="var(--veg-tag)"/></svg>
      <span class="flavor-tag__name">VEGETABLE</span>
      <span class="flavor-tag__sub">FLAVOR</span>
    </div>
    <div class="claims">
      <div class="claim">NATURAL INGREDIENTS <svg viewBox="0 0 15 15" aria-hidden="true"><rect x="1" y="3" width="11" height="11" fill="none" stroke="#fff" stroke-width="1.5"/><path d="M4 8 L7 11 L14 1" fill="none" stroke="#fff" stroke-width="2"/></svg></div>
      <div class="claim">GLUTEN FREE <svg viewBox="0 0 15 15" aria-hidden="true"><rect x="1" y="3" width="11" height="11" fill="none" stroke="#fff" stroke-width="1.5"/><path d="M4 8 L7 11 L14 1" fill="none" stroke="#fff" stroke-width="2"/></svg></div>
    </div>
    <svg class="product-photo" viewBox="0 0 290 192" role="img" aria-label="Photo of a white bowl of vegetable soup on a square plate">
      <defs><radialGradient id="veg-photo"><stop offset="0" stop-color="var(--veg-bowl)"/><stop offset=".6" stop-color="#f3f3ee"/><stop offset="1" stop-color="#e4e6dd" stop-opacity="0"/></radialGradient></defs>
      <ellipse cx="145" cy="96" rx="145" ry="96" fill="url(#veg-photo)"/>
    </svg>
    <div class="net-weight">NET WT.<br>9 OZ (150 MG)</div>
  </section>

  <section class="label label--chicken">
    <svg class="label__sweep" viewBox="0 0 1065 352" preserveAspectRatio="none" aria-hidden="true">
      <defs>
        <linearGradient id="chk-sweep" x1="0" y1="1" x2="1" y2="0">
          <stop offset="0" stop-color="var(--chk-light)"/>
          <stop offset="1" stop-color="var(--chk-bright)"/>
        </linearGradient>
      </defs>
      <path d="M650 352 C690 250 820 175 1065 140 L1065 352 Z" fill="url(#chk-sweep)"/>
    </svg>
    <h3 class="instruction-heading">INSTRUCTION</h3>
    <div class="nutrition-panel"><h3 class="nutrition-panel__title">NUTRITION FACTS</h3></div>
    <div class="brand-name">Wexley Pantry</div>
    <div class="title">
      <span class="title__instant">INSTANT</span>
      <span class="title__broth">Broth</span>
      <span class="title__sub">for Ramen and Soups</span>
    </div>
    <div class="flavor-tag">
      <svg viewBox="0 0 130 44" aria-hidden="true"><path d="M0 12 L128 0 L120 36 L4 44 Z" fill="var(--chk-tag)"/></svg>
      <span class="flavor-tag__name">CHICKEN</span>
      <span class="flavor-tag__sub">FLAVOR</span>
    </div>
    <div class="claims">
      <div class="claim">NATURAL INGREDIENTS <svg viewBox="0 0 15 15" aria-hidden="true"><rect x="1" y="3" width="11" height="11" fill="none" stroke="#fff" stroke-width="1.5"/><path d="M4 8 L7 11 L14 1" fill="none" stroke="#fff" stroke-width="2"/></svg></div>
      <div class="claim">GLUTEN FREE <svg viewBox="0 0 15 15" aria-hidden="true"><rect x="1" y="3" width="11" height="11" fill="none" stroke="#fff" stroke-width="1.5"/><path d="M4 8 L7 11 L14 1" fill="none" stroke="#fff" stroke-width="2"/></svg></div>
    </div>
    <svg class="product-photo" viewBox="0 0 290 192" role="img" aria-label="Photo of a white bowl of chicken noodle soup with dill on a square plate">
      <defs><radialGradient id="chk-photo"><stop offset="0" stop-color="var(--chk-bowl)"/><stop offset=".6" stop-color="#f5f3ee"/><stop offset="1" stop-color="#eee4cf" stop-opacity="0"/></radialGradient></defs>
      <ellipse cx="145" cy="96" rx="145" ry="96" fill="url(#chk-photo)"/>
    </svg>
    <div class="net-weight">NET WT.<br>9 OZ (150 MG)</div>
  </section>

</main>
</body>
</html>
```